Panama-Machu-Amazon tripanel brochure

Trifold brochure highlighting a tour to three bucket-list destinations at three times in the upcoming calendar year. This brochure needs to target both travel agents (who will provide the passengers) and the passengers too. Because three completely different locations are being sold, are five photos enough?I have many close-up detail photos of colorful tropical birds, orchids, monkeys, caiman, llamas that may be of assistance to the graphic artist. Email me at RBrenn5172@mailvane.com for additonal material.

Target Market(s)

Travel Agents, secondary target: potential passengers

Industry/Entity Type

Travel

Requirements
Must have
• Three great destinations-one fantastic tour-super low prices.

Panama Canal-Machu Picchu-Amazon

September 20-28, 2013 (Amazon extension to Oct. 3), January 17-25, 2014 (Amazon extension to January 30), May 16-24, 2014 (Amazon extension to May 29)

Only $2999 (Amazon extension $799), double occupancy. ($2599 from and return to Panama for non-Central Florida guests.)

Full details and itinerary at www.DaleWorthingtonTrips.com

DALE WORTHINGTON TRIPS LLC is bonded, insured, and registered with the State of Florida as a Seller of Travel. Registration No. ST52947.

Dale Worthington Trips LLC, 418 Bellmont Lane
Edgewater FL 32587-2261. Email RBrenn5172@mailvane.com
or call 386 527-9163

Nice to have
• Cost $2999, double occupancy, includes air transportation from Orlando, ground transfers, lodging including Panama Canal Tour, Machu Picchu, and city tours in Lima and Cuzco. ($2599 from and return to Panama.) Amazon extension $799, double occupancy, includes flight to Puerto Maldonado, lodging, transfers, Amazonia tour. Food limited to that provided gratis by hostelries; additional tours at the discretion of passengers. See www.DaleWorthingtonTrips.com for complete itinerary and details.

Dale Worthington Trips LLC to Mexico, Central America and South America since 1996.

```html
<!DOCTYPE html>
<html lang="en">
<head>
<meta charset="utf-8">
<title>Panama Canal Machu Picchu Amazon brochure</title>
<link href="https://fonts.googleapis.com/css2?family=Arimo:wght@400;700&display=swap" rel="stylesheet">
<style>
:root{
  --leaf:#6e9a2b;
  --leaf-dark:#587d1f;
  --sun:#f3e24a;
  --ink:#1c1c1c;
  --paper:#ffffff;
  --sky:#7fa8c9;
  --stone:#8c8a7a;
  --jungle:#3f6a2e;
  --macaw:#b8352a;
}
*{box-sizing:border-box;margin:0;padding:0}
html,body{width:779px;height:1200px;overflow:hidden;background:var(--paper)}
body{font-family:"Arimo",Arial,sans-serif;color:var(--ink);position:relative}
.panel{position:absolute;overflow:hidden}
.cover-side{left:0;top:0;width:260px;height:600px;background:var(--paper)}
.cost-block{position:absolute;left:0;top:0;width:260px;height:390px;background:var(--leaf);color:var(--paper);padding:22px 16px;font-size:12px;line-height:1.4}
.cost-block p{margin-bottom:12px}
.cost-block strong{color:var(--paper)}
.guide-photo{position:absolute;left:16px;top:402px;width:88px;height:64px;background:linear-gradient(#c9b79a,#6f6252)}
.guide-bio{position:absolute;left:16px;top:472px;width:230px;font-size:11.5px;line-height:1.35}
.guide-bio b{font-weight:700}
.middle{left:260px;top:0;width:260px;height:600px;background:var(--paper);text-align:center}
.notice{position:absolute;left:14px;top:14px;width:232px;font-size:12px;line-height:1.4;font-weight:700}
.band{position:absolute;left:0;top:148px;width:260px;height:28px;background:var(--leaf)}
.address{position:absolute;left:14px;top:192px;width:232px;font-size:12px;line-height:1.45;font-weight:700}
.site{position:absolute;left:0;top:398px;width:260px;font-size:11.5px;font-weight:700}
.cover{left:520px;top:0;width:259px;height:600px;background:var(--paper)}
.macaw{position:absolute;left:0;top:0;width:259px;height:385px;background:linear-gradient(160deg,#7ca53a 0%,var(--macaw) 45%,#2f6db0 75%,#5d8a2b 100%)}
.dates{position:absolute;right:14px;top:248px;width:200px;text-align:right;color:var(--paper);font-size:11.5px;line-height:1.35}
.dates b{font-size:12.5px}
.since{position:absolute;left:0;top:392px;width:259px;padding:10px 14px;text-align:center;font-size:12px;font-weight:700;line-height:1.4;background:var(--paper);border-top:26px solid var(--leaf)}
.title{position:absolute;left:0;top:520px;width:259px;text-align:center;color:var(--leaf-dark);font-size:24px;line-height:1.15;font-weight:700}
.photos{position:absolute;left:0;top:600px;width:779px;height:296px}
.photo{position:absolute;top:0;height:296px}
.ph-canal{left:0;width:260px;background:linear-gradient(#9fc0dd,var(--sky) 45%,#4d7496)}
.ph-picchu{left:260px;width:260px;background:linear-gradient(#b9c8d6,#6f8a5a 50%,var(--stone))}
.ph-jungle{left:520px;width:259px;background:linear-gradient(#6b8f4c,var(--jungle) 60%,#6a5a3b)}
.ph-boat{position:absolute;left:560px;top:760px;width:90px;height:62px;background:linear-gradient(#8aa4b8,#5e6f52)}
.itinerary{position:absolute;left:0;top:896px;width:779px;height:304px;background:var(--leaf);color:var(--paper);font-size:10px;line-height:1.35}
.col{position:absolute;top:8px;width:240px}
.col h2{color:var(--sun);font-size:12px;font-weight:700;margin-bottom:2px}
.col p{margin-bottom:4px}
.col b{color:var(--sun)}
</style>
</head>
<body>

<section class="panel cover-side">
  <div class="cost-block">
    <p><strong>Cost $2999</strong>, double occupancy, includes air transportation from Orlando, ground transfers, lodging including Panama Canal Tour, Machu Picchu, and city tours in Lima and Cuzco. ($2599 from and return to Panama.)</p>
    <p><strong>Amazon extension $799</strong>, double occupancy, includes flight to Puerto Maldonado, lodging, transfers, Amazonia tour. Food limited to that provided gratis by hostelries; additional tours at the discretion of passengers.</p>
    <p>See www.DaleWorthingtonTrips.com for complete itinerary and details.</p>
  </div>
  <div class="guide-photo" role="img" aria-label="Portrait photo of the tour leader"></div>
  <p class="guide-bio"><b>Dale Worthington</b> was Professor of Humanities and Communications at Coastal Ridge University in Daytona Beach, where he taught for 28 years, until retirement in 2012. For the past sixteen years he has led student and adult groups on tours of Latin America. He has written two books on the area.</p>
</section>

<section class="panel middle">
  <p class="notice">Dale Worthington Trips LLC<br>is bonded, insured, and registered with the State of Florida as a Seller of Travel. Registration No. ST52947.</p>
  <div class="band"></div>
  <p class="address">Dale Worthington Trips LLC<br>418 Bellmont Lane<br>Edgewater FL 32587-2261<br>Email RBrenn5172@mailvane.com<br>Call 386 527-9163</p>
  <p class="site">http://www.daleworthingtontrips.com/</p>
</section>

<section class="panel cover">
  <div class="macaw" role="img" aria-label="Close-up photo of a scarlet macaw in green foliage"></div>
  <p class="dates"><b>September 20-28, 2013</b><br>Amazon extension to Oct. 3<br><b>January 17-25, 2014</b><br>Amazon extension to January 30<br><b>May 16-24, 2014</b><br>Amazon extension to May 29</p>
  <p class="since">Dale Worthington Trips LLC<br>to Mexico, Central America<br>and South America since 1996</p>
  <h1 class="title">Panama Canal<br>Machu Picchu<br>Amazon</h1>
</section>

<div class="photos">
  <div class="photo ph-canal" role="img" aria-label="Photo of a ship passing through the Panama Canal"></div>
  <div class="photo ph-picchu" role="img" aria-label="Photo of the Machu Picchu ruins and mountains"></div>
  <div class="photo ph-jungle" role="img" aria-label="Photo of the Amazon rainforest river bank"></div>
</div>
<div class="ph-boat" role="img" aria-label="Photo of a river boat on the Amazon"></div>

<section class="itinerary">
  <div class="col" style="left:12px">
    <h2>Panama Canal–Machu Picchu</h2>
    <p><b>September 20-28, 2013</b><br>(Amazon Extension to Oct. 3)</p>
    <p><b>Friday.</b> Arrive by mid-afternoon flight from Orlando; hotel check-in and welcome dinner in Panama City. ($2599 guests from Panama join us here.)</p>
    <p><b>Saturday, September 21.</b> Transit the Panama Canal from the Pacific to the Atlantic, a distance of fifty miles, then visit the locks museum and the old quarter of the city before dinner.</p>
    <p><b>Sunday.</b> Transfer to Lima. Spend the afternoon and evening exploring the colonial center, the cathedral and the seaside cliffs of Miraflores.</p>
    <p><b>Monday.</b> Tour Lima.</p>
  </div>
  <div class="col" style="left:272px">
    <p><b>Tuesday.</b> Transfer to Cuzco and on to Ollantaytambo and the Sacred Valley. By rail across the high Andes.</p>
    <p><b>Visit the town of Ollantaytambo</b> at your leisure, which will prepare you for the splendor of Machu Picchu. Then go on by train to Machu Picchu village.</p>
    <p><b>Wednesday.</b> Machu Picchu. Met by our guide for a morning among the terraces and temples; afternoon free to hike or rest. We return to Cuzco in the afternoon train.</p>
    <p><b>Thursday and Friday.</b> Cuzco city tour with the cathedral and local sites, markets and Inca walls.</p>
    <p><b>Saturday.</b> Fly from Cuzco to Lima and on to Orlando.</p>
    <p>Arrive Orlando 10:55 PM</p>
  </div>
  <div class="col" style="left:530px">
    <h2>Amazon Extension</h2>
    <p><b>Saturday.</b> Arrive at Puerto Maldonado by river boat. Trip to the lodge. Your first evening walk in the rainforest in search of caiman and night birds.</p>
    <p><b>Sunday.</b> Hike and canoe trip to Sandoval Lake, known for giant otters, then a visit to a parrot clay lick. Dinner at the lodge.</p>
    <p><b>Monday.</b> Spend two nights at rustic but comfortable lodge in rainforest settings. Canopy tower at sunrise, then an afternoon with local guides.</p>
    <p><b>Tuesday.</b> Return to Puerto Maldonado. Evening stroll through town and market, last dinner in the jungle region.</p>
    <p><b>Wednesday.</b> Fly to Cuzco. Spend night in Lima and return to Orlando on Thursday.</p>
  </div>
</section>

</body>
</html>
```